Sharepoint Banners and Header design

I need some Sharepoint Extended headers and some fixed graphics made for our intranet site.

The intranet is for the school (not the strategic plan) and the words and graphics in the two designs should be complementary as they are on the same page (avoid large amounts of duplication).

I have created a mockup of a new intranet, showing a cropped photo where the header would fit. I have also inserted snippets of some plans where i would like a graphic that highlights our focus areas for the year, our values and our motto 'Strive to Accomplish'.

I would like the graphic to highlight the following (See the image titled example for header):

2021 Explicit Improvement Focus:
- Curriculum
- Consistency
- Knowing our Learners

Our values (Please use the design idea in the example header, where there is one C and the words are listed after it).
- Consideration
- Cooperation
- Courtesy
- Commitment
- Common Sense

2020 - 2023 Strategic Priorities (using the icons from the strategic plan)
- Written and Enacted Curriculum
- Community
- Growth
- Culture of Wellbeing

I have included examples of the type of graphic i am looking for, and an example of a header from the another school.

I have also included some images that might be useful.

I think the SharePoint extended header size is 2560 x 164

The graphic size is 1204 wide and should be landscape.

```html
<!DOCTYPE html>
<html lang="en">
<head>
<meta charset="utf-8">
<title>Intranet Banners</title>
<link href="https://fonts.googleapis.com/css2?family=Montserrat:wght@600;700&family=Hind:wght@600&display=swap" rel="stylesheet">
<style>
  :root {
    --navy: #3a4f86;
    --navy-dark: #2d3f70;
    --sky: #a9dcf3;
    --sky-mid: #55b1e2;
    --ink: #2a2a2a;
    --paper: #ffffff;
    --paper-tint: #f7f8fb;
    --divider: #8a8f99;
  }
  html, body {
    margin: 0;
    padding: 0;
    width: 1200px;
    height: 1200px;
    overflow: hidden;
    background: var(--paper);
  }
  .canvas {
    position: relative;
    width: 1200px;
    height: 1200px;
  }
  .banner {
    position: absolute;
    left: 156px;
    width: 896px;
    height: 122px;
    background: linear-gradient(180deg, var(--paper) 0%, var(--paper-tint) 100%);
    box-shadow: 2px 2px 3px rgba(0,0,0,0.45);
    overflow: hidden;
  }
  .banner--focus { top: 217px; }
  .banner--values { top: 555px; }
  .banner--priorities { top: 893px; }

  .banner__art {
    position: absolute;
    inset: 0;
    width: 896px;
    height: 122px;
  }
  .banner__title {
    position: absolute;
    top: 14px;
    height: 35px;
    background: var(--navy);
    color: var(--paper);
    font-family: "Montserrat", sans-serif;
    font-weight: 700;
    font-size: 19px;
    letter-spacing: 0.3px;
    line-height: 35px;
    text-align: center;
    margin: 0;
  }
  .banner--focus .banner__title,
  .banner--priorities .banner__title {
    left: 303px;
    width: 433px;
    clip-path: polygon(4% 0, 100% 0, 100% 100%, 0 100%);
    padding-left: 6px;
    box-sizing: border-box;
  }
  .banner--values .banner__title {
    left: 378px;
    width: 216px;
    clip-path: polygon(0 0, 100% 0, 96% 100%, 0 100%);
    padding-right: 8px;
    box-sizing: border-box;
  }

  .item {
    position: absolute;
    transform: translateX(-50%);
    display: flex;
    flex-direction: column;
    align-items: center;
    font-family: "Hind", sans-serif;
    font-weight: 600;
    color: var(--ink);
    white-space: nowrap;
  }
  .item__icon {
    width: 34px;
    height: 34px;
    display: block;
  }
  .banner--focus .item { top: 60px; font-size: 12.5px; }
  .banner--focus .item__label { margin-top: 1px; }
  .banner--values .item { top: 63px; font-size: 10.5px; }
  .banner--values .item__icon { width: 30px; height: 30px; }
  .banner--priorities .item { top: 62px; font-size: 9.5px; }
  .banner--priorities .item__icon { width: 28px; height: 28px; }
  .banner--priorities .item__label { margin-top: 3px; }

  .divider {
    position: absolute;
    width: 0;
    border-left: 1px dashed var(--divider);
  }
  .banner--focus .divider { top: 64px; height: 44px; }
  .banner--values .divider { top: 67px; height: 38px; }
  .banner--priorities .divider { top: 66px; height: 44px; }

  .school-name {
    position: absolute;
    top: 24px;
    width: 92px;
    display: flex;
    flex-direction: column;
    align-items: center;
    gap: 6px;
    font-family: "Montserrat", sans-serif;
    font-weight: 700;
    font-size: 13px;
    line-height: 1.15;
    color: var(--navy);
    text-align: center;
  }
  .school-name__mark {
    width: 34px;
    height: 34px;
    border-radius: 50%;
    background: var(--sky);
  }
  .banner--focus .school-name,
  .banner--priorities .school-name { left: 770px; }
  .banner--values .school-name { left: 25px; }
</style>
</head>
<body>
<main class="canvas">

  <!-- Explicit Improvement Focus -->
  <section class="banner banner--focus">
    <svg class="banner__art" viewBox="0 0 896 122" aria-hidden="false">
      <defs>
        <linearGradient id="focusPhoto" x1="0" y1="0" x2="1" y2="1">
          <stop offset="0" stop-color="#6f7f55"/>
          <stop offset="0.5" stop-color="#9aa783"/>
          <stop offset="1" stop-color="#8ea2c9"/>
        </linearGradient>
      </defs>
      <polygon points="0,0 334,0 278,122 0,122" fill="url(#focusPhoto)" role="img" aria-label="Photo of two smiling students in school uniform outdoors"/>
      <polygon points="334,0 357,0 301,122 278,122" fill="var(--sky)"/>
      <polygon points="298,60 308,60 288,106 278,106" fill="var(--navy)"/>
      <polygon points="310,66 318,66 296,114 288,114" fill="var(--sky-mid)"/>
    </svg>
    <h2 class="banner__title">Explicit Improvement Focus 2021</h2>

    <div class="item" style="left:369px">
      <svg class="item__icon" viewBox="0 0 36 36"><circle cx="18" cy="18" r="16" fill="#fff" stroke="var(--sky-mid)" stroke-width="2.5"/><rect x="12" y="10" width="12" height="16" fill="none" stroke="#555" stroke-width="1.3"/><path d="M14.5 14h7M14.5 17h7M14.5 20h5" stroke="#555" stroke-width="1.2"/></svg>
      <span class="item__label">Curriculum</span>
    </div>
    <span class="divider" style="left:439px"></span>
    <div class="item" style="left:508px">
      <svg class="item__icon" viewBox="0 0 36 36"><circle cx="18" cy="18" r="16" fill="#fff" stroke="var(--sky-mid)" stroke-width="2.5"/><circle cx="18" cy="18" r="6" fill="none" stroke="#555" stroke-width="1.3"/><circle cx="18" cy="18" r="2" fill="#555"/><path d="M18 9v3M18 24v3M9 18h3M24 18h3" stroke="#555" stroke-width="1.3"/></svg>
      <span class="item__label">Consistency</span>
    </div>
    <span class="divider" style="left:578px"></span>
    <div class="item" style="left:671px">
      <svg class="item__icon" viewBox="0 0 36 36"><circle cx="18" cy="18" r="16" fill="#fff" stroke="var(--sky-mid)" stroke-width="2.5"/><circle cx="18" cy="14" r="3" fill="none" stroke="#555" stroke-width="1.3"/><path d="M12 25c0-4 3-6 6-6s6 2 6 6z" fill="none" stroke="#555" stroke-width="1.3"/><rect x="10" y="20" width="16" height="6" fill="none" stroke="#555" stroke-width="1.1"/></svg>
      <span class="item__label">Knowing our Learners</span>
    </div>

    <div class="school-name">
      <span class="school-name__mark"></span>
      <span>Fernvale High</span>
    </div>
  </section>

  <!-- Our values -->
  <section class="banner banner--values">
    <svg class="banner__art" viewBox="0 0 896 122">
      <defs>
        <linearGradient id="valuesPhoto" x1="0" y1="0" x2="1" y2="1">
          <stop offset="0" stop-color="#2f4a2c"/>
          <stop offset="0.5" stop-color="#4f6b45"/>
          <stop offset="1" stop-color="#8fa9d4"/>
        </linearGradient>
      </defs>
      <polygon points="540,0 563,0 619,122 596,122" fill="var(--sky)"/>
      <polygon points="563,0 896,0 896,122 619,122" fill="url(#valuesPhoto)" role="img" aria-label="Photo of a smiling student in school uniform among green plants"/>
      <polygon points="578,62 588,62 608,106 598,106" fill="var(--navy)"/>
      <polygon points="566,70 574,70 596,116 588,116" fill="var(--sky-mid)"/>
    </svg>
    <div class="school-name">
      <span class="school-name__mark"></span>
      <span>Fernvale High</span>
    </div>
    <h2 class="banner__title">Our values</h2>

    <div class="item" style="left:173px">
      <svg class="item__icon" viewBox="0 0 36 36"><circle cx="18" cy="18" r="16" fill="#fff" stroke="var(--sky-mid)" stroke-width="2.5"/><path d="M13 26v-5c-2-2-2-9 5-10 6 0 7 5 5 8l1 3h-2v4" fill="none" stroke="#555" stroke-width="1.3"/><circle cx="18" cy="16" r="2.5" fill="none" stroke="#555" stroke-width="1.1"/></svg>
      <span class="item__label">Consideration</span>
    </div>
    <span class="divider" style="left:221px"></span>
    <div class="item" style="left:263px">
      <svg class="item__icon" viewBox="0 0 36 36"><circle cx="18" cy="18" r="16" fill="#fff" stroke="var(--sky-mid)" stroke-width="2.5"/><path d="M9 17l5-4 4 2 4-2 5 4-6 6-3-2-3 2z" fill="none" stroke="#555" stroke-width="1.3"/></svg>
      <span class="item__label">Cooperation</span>
    </div>
    <span class="divider" style="left:308px"></span>
    <div class="item" style="left:344px">
      <svg class="item__icon" viewBox="0 0 36 36"><circle cx="18" cy="18" r="16" fill="#fff" stroke="var(--sky-mid)" stroke-width="2.5"/><rect x="10" y="11" width="16" height="11" fill="none" stroke="#555" stroke-width="1.3"/><path d="M15 26h6M18 22v4" stroke="#555" stroke-width="1.3"/></svg>
      <span class="item__label">Courtesy</span>
    </div>
    <span class="divider" style="left:384px"></span>
    <div class="item" style="left:430px">
      <svg class="item__icon" viewBox="0 0 36 36"><circle cx="18" cy="18" r="16" fill="#fff" stroke="var(--sky-mid)" stroke-width="2.5"/><rect x="11" y="10" width="11" height="15" fill="none" stroke="#555" stroke-width="1.3"/><path d="M13.5 14h6M13.5 17h6M13.5 20h4" stroke="#555" stroke-width="1.1"/><circle cx="24" cy="13" r="3" fill="none" stroke="#555" stroke-width="1.2"/></svg>
      <span class="item__label">Commitment</span>
    </div>
    <span class="divider" style="left:474px"></span>
    <div class="item" style="left:524px">
      <svg class="item__icon" viewBox="0 0 36 36"><circle cx="18" cy="18" r="16" fill="#fff" stroke="var(--sky-mid)" stroke-width="2.5"/><rect x="11" y="10" width="14" height="14" fill="none" stroke="#555" stroke-width="1.3"/><circle cx="18" cy="15" r="2.5" fill="none" stroke="#555" stroke-width="1.1"/><path d="M14 22c1-3 7-3 8 0" fill="none" stroke="#555" stroke-width="1.1"/></svg>
      <span class="item__label">Common Sense</span>
    </div>
  </section>

  <!-- Strategic Priorities -->
  <section class="banner banner--priorities">
    <svg class="banner__art" viewBox="0 0 896 122">
      <defs>
        <linearGradient id="prioritiesPhoto" x1="0" y1="0" x2="1" y2="1">
          <stop offset="0" stop-color="#4a6a80"/>
          <stop offset="0.6" stop-color="#587a90"/>
          <stop offset="1" stop-color="#3e5a70"/>
        </linearGradient>
      </defs>
      <polygon points="0,0 334,0 278,122 0,122" fill="url(#prioritiesPhoto)" role="img" aria-label="Photo of a group of students in uniform standing against a blue brick wall"/>
      <polygon points="334,0 357,0 301,122 278,122" fill="var(--sky)"/>
      <polygon points="298,60 308,60 288,106 278,106" fill="var(--navy)"/>
      <polygon points="310,66 318,66 296,114 288,114" fill="var(--sky-mid)"/>
    </svg>
    <h2 class="banner__title">Strategic Priorities 2023 - 2020</h2>

    <div class="item" style="left:391px">
      <svg class="item__icon" viewBox="0 0 36 36"><circle cx="18" cy="18" r="16" fill="#fff" stroke="var(--sky-mid)" stroke-width="2.5"/><rect x="12" y="10" width="11" height="15" fill="none" stroke="#555" stroke-width="1.3"/><path d="M14.5 14h6M14.5 17h6M14.5 20h4" stroke="#555" stroke-width="1.1"/><path d="M22 22l4-4" stroke="#555" stroke-width="1.5"/></svg>
      <span class="item__label">Written and Enacted Curriculum</span>
    </div>
    <span class="divider" style="left:479px"></span>
    <div class="item" style="left:523px">
      <svg class="item__icon" viewBox="0 0 36 36"><circle cx="18" cy="18" r="16" fill="#fff" stroke="var(--sky-mid)" stroke-width="2.5"/><circle cx="14" cy="14" r="2.2" fill="none" stroke="#555" stroke-width="1.2"/><circle cx="22" cy="14" r="2.2" fill="none" stroke="#555" stroke-width="1.2"/><path d="M10 22c1-4 7-4 8 0M18 22c1-4 7-4 8 0M10 25h16" fill="none" stroke="#555" stroke-width="1.2"/></svg>
      <span class="item__label">Community</span>
    </div>
    <span class="divider" style="left:569px"></span>
    <div class="item" style="left:604px">
      <svg class="item__icon" viewBox="0 0 36 36"><circle cx="18" cy="18" r="16" fill="#fff" stroke="var(--sky-mid)" stroke-width="2.5"/><path d="M11 25h15" stroke="#555" stroke-width="1.3"/><rect x="12" y="20" width="3" height="5" fill="#555"/><rect x="16.5" y="17" width="3" height="8" fill="#555"/><rect x="21" y="13" width="3" height="12" fill="#555"/></svg>
      <span class="item__label">Growth</span>
    </div>
    <span class="divider" style="left:636px"></span>
    <div class="item" style="left:697px">
      <svg class="item__icon" viewBox="0 0 36 36"><circle cx="18" cy="18" r="16" fill="#fff" stroke="var(--sky-mid)" stroke-width="2.5"/><circle cx="18" cy="12" r="2.2" fill="none" stroke="#555" stroke-width="1.2"/><path d="M12 17l6 2 6-2M18 19v4l-4 4M18 23l4 4" fill="none" stroke="#555" stroke-width="1.2"/></svg>
      <span class="item__label">Culture of Wellbeing</span>
    </div>

    <div class="school-name">
      <span class="school-name__mark"></span>
      <span>Fernvale High</span>
    </div>
  </section>

</main>
</body>
</html>
```